New design of skin care labels for a natural makeup company

Our company sells 100% natural makeup and also offers a small selection of skin care cosmetics which aren't fully organic but have natural ingredients where possible and made by hand in small batches.
We are an English company with Japanese influence in that our staff and company name are Japanese, we understand how natural cosmetics in Japan are a huge business as demanded by Japanese girls and we include some Japanese ingredients in our cosmetics though we are marketing and selling in the UK.
We want to re-design the labels for 6 lines of our skin care range of cosmetics. These would be a mix of toners, creams, gels & face wash. There are 3 label sizes HxW:
50 x 120 mm
65 x 130 mm
90 x 115 mm
Our products are priced between £10-£15 so not expensive but not drug store budget prices either. We want the new labels to portray:
More luxury than common every day counter products
More natural than chemically preserved, fragranced, artificial products
Show they are free from parabens/sulphates and possibly even announce hand made in England
They need to include the usual necessary information like ingredients, usage instructions, warnings, weights, contact details along with our logo which is trademarked so unfortunately can't be altered or recoloured as its a mono logo.
We are open to all your ideas but our instincts will probably favour something clean/clear looking rather than fussy - though not too minimalist. Our bottles are either clear or semi transparent so we might prefer a see-thru label to show off the product. However these are just ideas at the moment and we may decide against them after seeing your various designs.
Females who care more about what they put on their skin.
Cosmetics

```html
<!DOCTYPE html>
<html lang="en">
<head>
<meta charset="utf-8">
<title>Gentle Balancing Toner – Label Range</title>
<link rel="stylesheet" href="https://fonts.googleapis.com/css2?family=Noto+Serif:wght@400&family=Raleway:wght@300;400;600&display=swap">
<style>
  :root {
    --canvas: #ffffff;
    --ink: #2b2b2b;
    --ink-soft: #4a4a4a;
    --band: #fbd9a8;
    --lilac-bloom: #e9a6ea;
    --lilac-soft: #f6e2f6;
    --lilac-pale: #fdf6fd;
    --lilac-leaf: #c2b0e8;
    --lilac-leaf-soft: #e6ddf5;
    --mint-bloom: #9fe8e6;
    --mint-soft: #e2f6f4;
    --mint-pale: #f7fcfb;
    --mint-leaf: #a8e2be;
    --mint-leaf-soft: #e0f5e8;
    --lemon-bloom: #fbcf8f;
    --lemon-soft: #fdf0d2;
    --lemon-pale: #fffcf2;
    --lemon-leaf: #f9df96;
    --lemon-leaf-soft: #fdf4d8;
  }
  * { box-sizing: border-box; margin: 0; padding: 0; }
  html, body {
    width: 1200px; height: 763px; overflow: hidden;
    background: var(--canvas);
  }
  .stage { position: relative; width: 1200px; height: 763px; }

  .label {
    position: absolute;
    background: #fff;
    overflow: hidden;
    font-family: 'Raleway', sans-serif;
    color: var(--ink);
  }
  .label--large  { left: 314px; top: 54px;  width: 468px; height: 599px; }
  .label--mint   { left: 813px; top: 54px;  width: 210px; height: 271px; }
  .label--lemon  { left: 813px; top: 383px; width: 210px; height: 270px; }

  .label__art { position: absolute; left: 0; right: 0; }
  .label__band { position: absolute; left: 0; right: 0; background: var(--band); }

  .brand {
    position: absolute; left: 0; right: 0;
    display: flex; flex-direction: column; align-items: center;
    font-family: 'Raleway', sans-serif; font-weight: 600;
    color: var(--ink); letter-spacing: 0.12em;
  }
  .brand__dot { border-radius: 50%; border: 3px solid var(--ink); background: #fff; }

  .copy { position: absolute; left: 0; right: 0; text-align: center; }
  .copy__claim { font-weight: 300; color: var(--ink-soft); }
  .copy__product {
    font-family: 'Noto Serif', serif; font-weight: 400;
    color: var(--ink); white-space: nowrap; line-height: 1.15;
  }
  .copy__skin { font-weight: 400; color: var(--ink-soft); line-height: 1.35; }

  /* artwork tones: blossom area top, leaf area bottom */
  .label--large .label__art--top {
    background:
      radial-gradient(circle at 22% 42%, var(--lilac-bloom) 0, rgba(233,166,234,.55) 18%, transparent 42%),
      radial-gradient(ellipse at 85% 20%, var(--lilac-soft) 0, transparent 45%),
      radial-gradient(ellipse at 80% 95%, var(--lilac-leaf-soft) 0, transparent 40%),
      linear-gradient(135deg, var(--lilac-soft), var(--lilac-pale) 60%, var(--lilac-soft));
  }
  .label--large .label__art--bottom {
    background:
      radial-gradient(ellipse at 12% 70%, var(--lilac-leaf) 0, transparent 38%),
      radial-gradient(ellipse at 62% 45%, var(--lilac-leaf) 0, rgba(194,176,232,.5) 22%, transparent 48%),
      radial-gradient(ellipse at 92% 92%, var(--lilac-leaf) 0, transparent 30%),
      linear-gradient(160deg, var(--lilac-leaf-soft), #f6f2fb 50%, var(--lilac-leaf-soft));
  }
  .label--mint .label__art--top {
    background:
      radial-gradient(circle at 20% 45%, var(--mint-bloom) 0, rgba(159,232,230,.5) 20%, transparent 45%),
      linear-gradient(135deg, var(--mint-soft), var(--mint-pale) 60%, var(--mint-soft));
  }
  .label--mint .label__art--bottom {
    background:
      radial-gradient(ellipse at 15% 75%, var(--mint-leaf) 0, transparent 40%),
      radial-gradient(ellipse at 65% 40%, var(--mint-leaf) 0, transparent 45%),
      linear-gradient(160deg, var(--mint-leaf-soft), #f4fbf7 55%, var(--mint-leaf-soft));
  }
  .label--lemon .label__art--top {
    background:
      radial-gradient(circle at 20% 45%, var(--lemon-bloom) 0, rgba(251,207,143,.5) 20%, transparent 45%),
      linear-gradient(135deg, var(--lemon-soft), var(--lemon-pale) 60%, var(--lemon-soft));
  }
  .label--lemon .label__art--bottom {
    background:
      radial-gradient(ellipse at 15% 75%, var(--lemon-leaf) 0, transparent 40%),
      radial-gradient(ellipse at 65% 40%, var(--lemon-leaf) 0, transparent 45%),
      linear-gradient(160deg, var(--lemon-leaf-soft), var(--lemon-pale) 55%, var(--lemon-leaf-soft));
  }

  /* large label geometry */
  .label--large .label__art--top    { top: 0; height: 226px; }
  .label--large .label__art--bottom { top: 376px; bottom: 0; }
  .label--large .label__band--top    { top: 226px; height: 6px; }
  .label--large .label__band--bottom { top: 370px; height: 6px; }
  .label--large .brand { top: 8px; gap: 6px; font-size: 20px; }
  .label--large .brand__dot { width: 54px; height: 54px; }
  .label--large .copy { top: 256px; }
  .label--large .copy__claim { font-size: 17px; }
  .label--large .copy__product { font-size: 39px; margin-top: 0; }
  .label--large .copy__skin { font-size: 10.5px; margin-top: 8px; }

  /* small label geometry */
  .label--mint .label__art--top, .label--lemon .label__art--top { top: 0; height: 101px; }
  .label--mint .label__art--bottom, .label--lemon .label__art--bottom { top: 169px; bottom: 0; }
  .label--mint .label__band--top, .label--lemon .label__band--top { top: 101px; height: 4px; }
  .label--mint .label__band--bottom, .label--lemon .label__band--bottom { top: 165px; height: 4px; }
  .label--mint .brand, .label--lemon .brand { top: 4px; left: 0; gap: 3px; font-size: 9px; }
  .label--mint .brand__dot, .label--lemon .brand__dot { width: 24px; height: 24px; border-width: 2px; }
  .label--mint .copy, .label--lemon .copy { top: 109px; }
  .label--mint .copy__claim, .label--lemon .copy__claim { font-size: 8px; }
  .label--mint .copy__product, .label--lemon .copy__product { font-size: 17.5px; margin-top: 1px; }
  .label--mint .copy__skin, .label--lemon .copy__skin { font-size: 5px; margin-top: 3px; }
</style>
</head>
<body>
<main class="stage">

  <section class="label label--large">
    <div class="label__art label__art--top" role="img" aria-label="Soft lilac and pink floral pattern with a large stylised blossom"></div>
    <div class="label__band label__band--top"></div>
    <div class="brand"><span class="brand__dot"></span><span>HINATA</span></div>
    <div class="copy">
      <p class="copy__claim">Naturaly Calming &amp; Hydrating</p>
      <h1 class="copy__product">Gentle Balancing Toner</h1>
      <p class="copy__skin">All Skin Types<br>suitable for sensitive skin</p>
    </div>
    <div class="label__band label__band--bottom"></div>
    <div class="label__art label__art--bottom" role="img" aria-label="Lavender damask leaf and swirl pattern"></div>
  </section>

  <section class="label label--mint">
    <div class="label__art label__art--top" role="img" aria-label="Pale aqua floral pattern with a stylised blossom"></div>
    <div class="label__band label__band--top"></div>
    <div class="brand"><span class="brand__dot"></span><span>HINATA</span></div>
    <div class="copy">
      <p class="copy__claim">Naturaly Calming &amp; Hydrating</p>
      <h2 class="copy__product">Gentle Balancing Toner</h2>
      <p class="copy__skin">All Skin Types<br>suitable for sensitive skin</p>
    </div>
    <div class="label__band label__band--bottom"></div>
    <div class="label__art label__art--bottom" role="img" aria-label="Mint green damask leaf and swirl pattern"></div>
  </section>

  <section class="label label--lemon">
    <div class="label__art label__art--top" role="img" aria-label="Pale peach floral pattern with a stylised blossom"></div>
    <div class="label__band label__band--top"></div>
    <div class="brand"><span class="brand__dot"></span><span>HINATA</span></div>
    <div class="copy">
      <p class="copy__claim">Naturaly Calming &amp; Hydrating</p>
      <h2 class="copy__product">Gentle Balancing Toner</h2>
      <p class="copy__skin">All Skin Types<br>suitable for sensitive skin</p>
    </div>
    <div class="label__band label__band--bottom"></div>
    <div class="label__art label__art--bottom" role="img" aria-label="Soft yellow damask leaf and swirl pattern"></div>
  </section>

</main>
</body>
</html>
```